Business Card Design Project

We need a Business Card for an Mechanical Engineering firm in Singapore. The design should be Modern & Technical looking, yet eye catching.

Our company deals in Cutting Tools & Machine Accessories for the Manufacturing Industries such as Oil & Gas, Aero Space, etc... For more information on our Company, you can either email me or view our website www.valtrion.com.sg.

We are trying to revamp our image to give our consumers a fresh new perspective to our company, so we welcome all ideas.

Industry/Entity Type

Business

Requirements
Must have
• Must incorporate New Company Logo into the card as shown in Uploaded file.

```html
<!DOCTYPE html>
<html lang="en">
<head>
<meta charset="utf-8">
<title>Valtrion Tools – Business Card</title>
<link rel="stylesheet" href="https://fonts.googleapis.com/css2?family=Arimo:wght@400;700&display=swap">
<style>
  :root {
    --backdrop: #3a3a3a;
    --paper: #ffffff;
    --maroon: #8c0f34;
    --maroon-deep: #6e0a28;
    --ink: #111111;
    --ink-soft: #222222;
  }
  * { box-sizing: border-box; margin: 0; padding: 0; }
  html, body {
    width: 1192px; height: 1200px; overflow: hidden;
    background: var(--backdrop);
    font-family: "Arimo", Arial, sans-serif;
  }
  .canvas {
    width: 1192px; height: 1200px;
    display: flex; flex-direction: column; align-items: center; justify-content: center;
    gap: 40px;
  }
  .card {
    position: relative;
    width: 880px; height: 528px;
    box-shadow: 0 10px 30px rgba(0,0,0,.45);
  }
  .card--front { background: var(--paper); }
  .card--back { background: var(--maroon); }

  .wordmark {
    position: absolute;
    display: flex; align-items: center; gap: 14px;
    font-weight: 700; text-transform: uppercase; letter-spacing: 1px;
  }
  .wordmark__dot { border-radius: 50%; flex: none; }
  .card--front .wordmark { left: 150px; top: 92px; font-size: 46px; color: var(--maroon); }
  .card--front .wordmark__dot { width: 46px; height: 46px; background: var(--maroon); }
  .card--back .wordmark { left: 50%; top: 50%; transform: translate(-50%, -50%); font-size: 60px; color: var(--maroon-deep); }
  .card--back .wordmark__dot { width: 60px; height: 60px; background: var(--maroon-deep); }

  .holder { position: absolute; left: 110px; top: 290px; }
  .holder__name { font-size: 28px; font-weight: 700; color: var(--ink); }
  .holder__title { font-size: 20px; color: var(--ink-soft); margin-top: 4px; }

  .contact { position: absolute; left: 500px; top: 240px; color: var(--ink-soft); font-size: 19px; line-height: 1.25; }
  .contact__company { color: var(--maroon); font-weight: 700; }
  .contact__lines { list-style: none; margin-top: 22px; }
  .contact__lines li { display: flex; align-items: center; gap: 12px; }
  .contact__icon { width: 18px; height: 18px; flex: none; }
  .contact__web { display: block; margin-top: 26px; color: var(--maroon); font-size: 21px; text-decoration: none; }
</style>
</head>
<body>
<main class="canvas">
  <section class="card card--front">
    <div class="wordmark"><span class="wordmark__dot"></span>Valtrion Tools</div>

    <div class="holder">
      <p class="holder__name">Miranda</p>
      <p class="holder__title">Managing Director</p>
    </div>

    <address class="contact" style="font-style:normal">
      <p class="contact__company">Valtrion Tools Pte Ltd</p>
      <p>52 Kallang Way #03-12,<br>Northgate Industrial Hub,<br>Singapore 349261</p>
      <ul class="contact__lines">
        <li>
          <svg class="contact__icon" viewBox="0 0 18 18" aria-hidden="true"><circle cx="9" cy="9" r="9" fill="var(--maroon)"/><path d="M6 4.5l1.6 2.2-1 1c.6 1.3 1.5 2.2 2.8 2.8l1-1 2.2 1.6-.9 1.9c-3.6-.3-6.3-3-6.6-6.6z" fill="#fff"/></svg>
          Tel: 65-61234570
        </li>
        <li>
          <svg class="contact__icon" viewBox="0 0 18 18" aria-hidden="true"><circle cx="9" cy="9" r="9" fill="var(--maroon)"/><rect x="4.5" y="7" width="9" height="5" rx="1" fill="#fff"/><rect x="6" y="4.5" width="6" height="3" fill="#fff"/></svg>
          Fax: 65-61234571
        </li>
        <li>
          <svg class="contact__icon" viewBox="0 0 18 18" aria-hidden="true"><circle cx="9" cy="9" r="9" fill="var(--maroon)"/><rect x="4" y="5.5" width="10" height="7" fill="#fff"/><path d="M4 5.5l5 4 5-4" stroke="var(--maroon)" stroke-width="1.2" fill="none"/></svg>
          Email: info@valtrion.com.sg
        </li>
      </ul>
      <a class="contact__web" href="#">www.valtrion.com.sg</a>
    </address>
  </section>

  <section class="card card--back">
    <div class="wordmark"><span class="wordmark__dot"></span>Valtrion Tools</div>
  </section>
</main>
</body>
</html>
```